We need flyer to promote our new FMLA / Disability Form Completion Service.
CareVeldt is a Health Data Services company supporting Hospitals and Medical Practices in the secure electronic exchange, delivery and integration of protected health information (PHI). CareVeldt Services include Release of Information, Audit and Chart Review, Disability and Family and Medical Leave Act (FMLA) form processing, and revenue cycle support services.

I have attached some of the other collateral we have for our other service lines. We would like for the colour/imagery to somewhat coordinate with these.

For further reference about the company : www.careveldt-partners.example

The flyer we are hoping to receive is specific to the Disability and FMLA Form Processing (in Bold above). I’ve attached a copy of our workflow for your review. The value delivered to the client as a result of engaging this service is as follows:

-Reduce internal labor costs
-Improve quality
-Accelerate turnaround time
-Improve patient satisfaction
-Reduce internal phone traffic

CareVeldt manages all aspects of the FMLA form completion process including:

-Review for HIPAA compliance
-Completion of forms
-Communication with patient/requesting parties
-Signing off on forms (as approved by the client)
-Invoicing
Delivery
Tracking/Reporting

CareVeldt clients are provided complete transparency into all CareVeldt actions and documents for tracking and accountability purposes.

Target Market(s)

CareVeldt’s target market are Hospital Executives and Health Information Management Directors and Medical Practice Administrators.

Requirements
Must have
• Outline value of FMLA/Disability Form Completion Service:
• The value delivered to the client as a result of engaging this service is as follows:
• • Reduce internal labor costs
• • Improve quality
• • Accelerate turnaround time
• • Improve patient satisfaction
• • Reduce internal phone traffic
• CareVeldt manages all aspects of the FMLA form completion process including:
• • Review for HIPAA compliance
• • Completion of forms
• • Communication with patient/requesting parties
• • Signing off on forms (as approved by client)
• • Invoicing
• • Delivery
• • Tracking/Reporting
• CareVeldt clients are provided complete transparency into all CareVeldt actions and documents for tracking and accountability purposes.
Nice to have
• Similar imagery/colors as the current marketing materials being used on our website and the materials uploaded to this project.

```html
<!DOCTYPE html>
<html lang="en">
<head>
<meta charset="utf-8">
<title>CareVeldt Group – FMLA / Disability Form Processing Flyers</title>
<link rel="stylesheet" href="https://fonts.googleapis.com/css2?family=Anton&family=Oswald:wght@400;500;600&family=Roboto:wght@400;500&display=swap">
<style>
  :root{
    --green:#7aab2b;
    --green-dark:#5b8a1c;
    --green-light:#9cc64a;
    --grey-dark:#5f5b58;
    --grey:#77726e;
    --grey-light:#ebebeb;
    --text:#4a4846;
    --white:#ffffff;
    --backdrop:#d9d9d9;
  }
  *{box-sizing:border-box;margin:0;padding:0}
  html,body{width:1200px;height:1000px;overflow:hidden}
  body{background:var(--backdrop);font-family:"Roboto",Arial,sans-serif;color:var(--text);position:relative}
  .flyer{position:absolute;top:150px;width:540px;height:700px;background:var(--white);overflow:hidden;box-shadow:0 6px 18px rgba(0,0,0,.18)}
  .flyer--tech{left:40px}
  .flyer--service{left:620px}
  .flyer__art{position:absolute;inset:0;width:540px;height:700px}
  .brand{position:absolute;right:26px;display:flex;align-items:center;gap:8px;font-family:"Oswald",sans-serif;font-weight:500;font-size:28px;color:var(--green);letter-spacing:.5px}
  .brand__dot{width:14px;height:14px;border-radius:50%;background:var(--green)}
  .flyer--tech .brand{top:4px}
  .flyer--service .brand{top:10px}
  .headline{position:absolute;font-family:"Anton",sans-serif;color:var(--green);text-transform:uppercase;line-height:.98;letter-spacing:1px;text-shadow:2px 2px 0 var(--green-dark),3px 4px 6px rgba(0,0,0,.45)}
  .flyer--tech .headline{left:40px;top:225px;font-size:44px}
  .flyer--service .headline{left:28px;top:222px;font-size:40px}
  .section-title{font-family:"Oswald",sans-serif;font-weight:600;text-transform:uppercase;font-size:15px}
  .about{position:absolute;left:38px;top:470px;width:232px}
  .about .section-title{color:var(--green);margin-bottom:4px}
  .about p{font-size:8.4px;line-height:1.42;text-align:justify;color:var(--text)}
  .tech-box{position:absolute;left:300px;top:386px;width:208px;color:var(--white)}
  .tech-box .section-title{color:#3b3a36;font-size:14px;margin-bottom:4px}
  .tech-box p{font-size:8px;line-height:1.4;text-align:justify;margin-bottom:8px}
  .checklist{list-style:none}
  .checklist li{position:relative;padding-left:14px;font-size:9.4px;line-height:1.25;margin-bottom:4px}
  .checklist li::before{content:"";position:absolute;left:0;top:3px;width:6px;height:6px;background:var(--grey)}
  .flyer--service .checklist li{color:var(--text);font-size:9.4px;margin-bottom:2px}
  .flyer--service .checklist li::before{background:var(--green)}
  .contact{position:absolute;font-family:"Oswald",sans-serif;font-size:13px}
  .contact__row{display:flex;align-items:center;gap:7px;margin-bottom:5px}
  .contact__icon{width:13px;height:13px;border-radius:50%;background:var(--green);display:flex;align-items:center;justify-content:center;flex:none}
  .contact__icon svg{width:8px;height:8px}
  .connect{display:flex;align-items:center;gap:6px;font-size:9px;letter-spacing:.4px;margin-left:20px}
  .connect__mark{width:11px;height:11px;border-radius:2px;background:var(--green)}
  .flyer--tech .contact--direct{left:60px;top:628px;color:var(--grey-dark)}
  .flyer--tech .contact--web{left:306px;top:628px;color:var(--grey-dark)}
  .flyer--service .contact--direct{left:30px;top:614px;color:var(--white)}
  .flyer--service .contact--web{left:262px;top:626px;color:var(--white)}
  .service-copy{position:absolute;left:258px;top:340px;width:266px}
  .service-copy .intro{font-size:9.6px;color:var(--grey);margin-bottom:4px;line-height:1.3}
  .service-copy .checklist{margin-bottom:10px}
</style>
</head>
<body>

<article class="flyer flyer--tech">
  <svg class="flyer__art" viewBox="0 0 540 700">
    <defs>
      <linearGradient id="photoTech" x1="0" y1="0" x2="1" y2="1">
        <stop offset="0" stop-color="#b9c7d3"/>
        <stop offset=".5" stop-color="#e6ecf0"/>
        <stop offset="1" stop-color="#c8cfd4"/>
      </linearGradient>
      <linearGradient id="swoopTech" x1="0" y1="0" x2="0" y2="1">
        <stop offset="0" stop-color="#f3f3f3"/>
        <stop offset="1" stop-color="#ffffff"/>
      </linearGradient>
    </defs>
    <g role="img" aria-label="Photo of a nurse and a doctor reviewing forms on a tablet at a desk">
      <path d="M0 44 H300 L332 82 H540 V395 C420 430 240 470 0 430 Z" fill="url(#photoTech)"/>
    </g>
    <path d="M0 430 C240 470 420 430 540 395 V420 C420 458 240 500 0 468 Z" fill="var(--grey)"/>
    <path d="M0 468 C240 500 420 458 540 420 V700 H0 Z" fill="url(#swoopTech)"/>
    <rect x="286" y="372" width="236" height="246" rx="18" fill="var(--green)"/>
    <rect x="0" y="0" width="540" height="4" fill="var(--grey-light)"/>
  </svg>

  <div class="brand"><span class="brand__dot"></span>CareVeldt Group</div>

  <h1 class="headline">FMLA /<br>Disability<br>Form Processing</h1>

  <section class="tech-box">
    <h2 class="section-title">DocRelay™ Technology</h2>
    <p>CareVeldt’s proprietary software, DocRelay is a Software as a Service (SaaS) platform that enables medical facilities to effectively manage and monetize the ROI process. DocRelay provides the necessary tools to stay compliant with complex regulations while streamlining the disclosure process for all parties involved.</p>
    <ul class="checklist">
      <li>Reduced Overhead Expenses</li>
      <li>Secure PHI messaging</li>
      <li>Systematic e-delivery</li>
      <li>Robust Audit Logs and Reporting</li>
      <li>Accounting of Disclosure and Tracking</li>
      <li>Integration with Electronic Medical Record (EMR) systems</li>
    </ul>
  </section>

  <section class="about">
    <h2 class="section-title">About CareVeldt Group</h2>
    <p>Founded in 2006, CareVeldt Group is an industry leader providing health information management and technology services for medical clinics and hospitals. CareVeldt was founded based on the specific need to incorporate technology into the Release of Information (ROI) process. CareVeldt’s DocRelay software is revolutionizing the ROI industry as software designed to meet the need for a more efficient method of releasing medical records, while complying with increasingly restrictive HIPAA requirements.</p>
  </section>

  <div class="contact contact--direct">
    <div class="contact__row"><span class="contact__icon"><svg viewBox="0 0 10 10"><path d="M2 1 L4 1 L4.6 3 L3.6 3.8 C4.2 5 5 5.8 6.2 6.4 L7 5.4 L9 6 L9 8 C5 8.5 1.5 5 2 1 Z" fill="#fff"/></svg></span>1-800-555-0147</div>
    <div class="contact__row"><span class="contact__icon"><svg viewBox="0 0 10 10"><rect x="1" y="2.5" width="8" height="5" fill="none" stroke="#fff" stroke-width="1"/><path d="M1 2.5 L5 5.5 L9 2.5" fill="none" stroke="#fff" stroke-width="1"/></svg></span>Sales@CareVeldt-Partners.example</div>
  </div>
  <div class="contact contact--web">
    <div class="contact__row"><span class="contact__icon"><svg viewBox="0 0 10 10"><circle cx="5" cy="5" r="3.6" fill="none" stroke="#fff" stroke-width="1"/><path d="M1.4 5 H8.6 M5 1.4 V8.6" stroke="#fff" stroke-width=".8"/></svg></span>www.careveldt-partners.example</div>
    <div class="connect">CONNECT WITH US <span class="connect__mark"></span></div>
  </div>
</article>

<article class="flyer flyer--service">
  <svg class="flyer__art" viewBox="0 0 540 700">
    <defs>
      <linearGradient id="photoService" x1="0" y1="0" x2="1" y2="0">
        <stop offset="0" stop-color="#d4dde3"/>
        <stop offset=".6" stop-color="#eef2f4"/>
        <stop offset="1" stop-color="#b8c6cf"/>
      </linearGradient>
      <linearGradient id="panelService" x1="0" y1="0" x2="1" y2="0">
        <stop offset="0" stop-color="#f4f4f4"/>
        <stop offset="1" stop-color="#e2e2e2"/>
      </linearGradient>
    </defs>
    <g role="img" aria-label="Photo of three young clinicians in white coats looking at a computer screen">
      <path d="M0 44 H232 L262 96 H540 V318 H0 Z" fill="url(#photoService)"/>
    </g>
    <rect x="0" y="318" width="540" height="12" fill="var(--green)"/>
    <rect x="245" y="330" width="295" height="270" fill="url(#panelService)"/>
    <rect x="18" y="344" width="206" height="120" fill="var(--green)"/>
    <g role="img" aria-label="Photo of a hand using a tablet showing patient records">
      <rect x="23" y="349" width="196" height="110" fill="#6b6e72"/>
    </g>
    <rect x="18" y="476" width="206" height="114" fill="var(--green)"/>
    <g role="img" aria-label="Illustration of a clinician holding a tablet beside a digital health display">
      <rect x="23" y="481" width="196" height="104" fill="#bfe3ec"/>
    </g>
    <rect x="0" y="600" width="540" height="86" fill="var(--grey)"/>
    <rect x="0" y="686" width="540" height="14" fill="var(--green)"/>
  </svg>

  <div class="brand"><span class="brand__dot"></span>CareVeldt Group</div>

  <h1 class="headline">FMLA / Disability<br>Form Processing</h1>

  <section class="service-copy">
    <p class="intro">CareVeldt Service adds value to your practice</p>
    <ul class="checklist">
      <li>Reduced Overhead Expenses</li>
      <li>Secure PHI messaging</li>
      <li>Systematic E-Delivery</li>
      <li>Robust Audit Logs and Reporting</li>
      <li>Accounting of Disclosure and Tracking</li>
      <li>Integration with Electronic Medical Record</li>
    </ul>
    <p class="intro">CareVeldt manages all aspects of the FMLA form completion process including:</p>
    <ul class="checklist">
      <li>Review for HIPAA compliance</li>
      <li>Completion of forms</li>
      <li>Communication with patient/requesting parties</li>
      <li>Signing off on forms (as approved by the client)</li>
      <li>Invoicing</li>
      <li>Delivery</li>
      <li>Tracking/Reporting</li>
      <li>Absolute transparency to clients via DocRelay</li>
    </ul>
  </section>

  <div class="contact contact--direct">
    <div class="contact__row"><span class="contact__icon"><svg viewBox="0 0 10 10"><path d="M2 1 L4 1 L4.6 3 L3.6 3.8 C4.2 5 5 5.8 6.2 6.4 L7 5.4 L9 6 L9 8 C5 8.5 1.5 5 2 1 Z" fill="#fff"/></svg></span>1-800-555-0147</div>
    <div class="contact__row"><span class="contact__icon"><svg viewBox="0 0 10 10"><rect x="1" y="2.5" width="8" height="5" fill="none" stroke="#fff" stroke-width="1"/><path d="M1 2.5 L5 5.5 L9 2.5" fill="none" stroke="#fff" stroke-width="1"/></svg></span>Sales@CareVeldt-Partners.example</div>
  </div>
  <div class="contact contact--web">
    <div class="contact__row"><span class="contact__icon"><svg viewBox="0 0 10 10"><circle cx="5" cy="5" r="3.6" fill="none" stroke="#fff" stroke-width="1"/><path d="M1.4 5 H8.6 M5 1.4 V8.6" stroke="#fff" stroke-width=".8"/></svg></span>www.careveldt-partners.example</div>
    <div class="connect">CONNECT WITH US <span class="connect__mark"></span></div>
  </div>
</article>

</body>
</html>
```